Volunteer fire fighters needed banner

As part of our recruitment campaign, we need a sign we can post on our sign trailer to entice locals to join our volunteer fire service. This design will be printed on a banner, front and back, to catch traffic going in both directions on a busy roadway. This banner will have a printed surface of 4 feet tall by 8 feet long.
Our fire department is looking to attract people between the ages of 18 and 35 years old who are interested in being a firefighter. We offer our volunteers:
-Free professional training
-All equipment supplied
-Tax abatements for active volunteers
For more information, you can check us out at:
Brookmerecrestfire.example

This design should:
-scale to and fit a 4'x8' canvas
-Include our web address "BrookmereCrestFire.example"
-Say "Members Wanted"
-"Drill every Tuesday at 7pm"
-"37 Quarry Bend Lane"
-Include "Brookmere Crest Fire Department"

We've included reference photos and past images we use for our other campaigns for inspiration for you.

Target Market(s)

18-35 y/o

Industry/Entity Type

Fire Service

Requirements
Must have
• -scale to and fit a 4'x8' canvas -Include our web address "BrookmereCrestFire.example" -Say "Members Wanted" -"Drill every Tuesday at 7pm" -"37 Quarry Bend Lane" -Include "Brookmere Crest Fire Department"

```html
<!DOCTYPE html>
<html lang="en">
<head>
<meta charset="utf-8">
<title>Members Wanted – Brookmere Crest Fire Department</title>
<link href="https://fonts.googleapis.com/css2?family=Archivo+Black&family=Montserrat:wght@600;700;800&display=swap" rel="stylesheet">
<style>
  :root{
    --navy:#232f8f;
    --navy-deep:#1c2a6e;
    --red:#d8202a;
    --red-bright:#ec2f3a;
    --paper:#f4f4f5;
    --paper-shade:#d9dadd;
    --ink:#222226;
    --white:#ffffff;
    --stage:#e6e8ec;
  }
  *{margin:0;padding:0;box-sizing:border-box}
  html,body{width:1067px;height:1200px;overflow:hidden;background:var(--stage)}
  .banner{
    position:absolute;left:33px;top:350px;width:1000px;height:500px;overflow:hidden;
    background:radial-gradient(ellipse at 40% 30%,var(--paper) 40%,var(--paper-shade) 100%);
    box-shadow:0 6px 24px rgba(0,0,0,.18);
  }
  .banner-shapes{position:absolute;inset:0;width:100%;height:100%}
  .truck-photo{
    position:absolute;left:640px;top:130px;width:360px;height:340px;
    background:radial-gradient(ellipse at 50% 50%,#e5313a 0%,#b4202a 45%,rgba(60,40,45,.85) 75%,rgba(60,40,45,0) 100%);
  }
  .headline{
    position:absolute;left:28px;font-family:"Archivo Black",sans-serif;
    font-size:108px;line-height:1;letter-spacing:-1px;text-transform:uppercase;white-space:nowrap;
  }
  .headline--top{top:22px;color:var(--navy)}
  .headline--bottom{top:128px;color:var(--red)}
  .drill-band{
    position:absolute;left:0;top:254px;width:620px;height:42px;background:var(--navy);
    color:var(--white);font-family:"Montserrat",sans-serif;font-weight:700;font-size:29px;
    line-height:42px;padding-left:28px;letter-spacing:.3px;white-space:nowrap;
  }
  .address{
    position:absolute;left:28px;top:306px;display:flex;align-items:center;gap:10px;
    font-family:"Montserrat",sans-serif;font-weight:800;font-size:25px;letter-spacing:2.5px;
    color:var(--ink);text-transform:uppercase;white-space:nowrap;
  }
  .address svg{width:22px;height:27px}
  .web{
    position:absolute;left:28px;top:426px;height:44px;display:flex;align-items:center;gap:14px;
    font-family:"Montserrat",sans-serif;font-weight:800;font-size:31px;color:var(--red);white-space:nowrap;
  }
  .web svg{width:28px;height:28px}
  .dept-name{
    position:absolute;left:786px;top:22px;width:194px;display:flex;align-items:flex-start;gap:8px;
    font-family:"Montserrat",sans-serif;font-weight:800;font-size:16px;line-height:1.2;
    color:var(--navy);text-transform:uppercase;
    background:rgba(255,255,255,.92);padding:12px;
  }
  .dept-name .dot{flex:none;width:14px;height:14px;border-radius:50%;background:var(--red);margin-top:2px}
</style>
</head>
<body>
  <section class="banner" aria-label="Volunteer firefighter recruitment banner">
    <svg class="banner-shapes" viewBox="0 0 1000 500" preserveAspectRatio="none" aria-hidden="true">
      <polygon points="0,360 700,402 1000,402 1000,500 0,500" fill="var(--navy)"/>
      <polygon points="0,330 700,402 0,360" fill="var(--red)"/>
      <polygon points="0,422 640,422 670,474 0,474" fill="var(--white)"/>
    </svg>

    <div class="truck-photo" role="img" aria-label="Photo of a red fire engine with chrome grille"></div>

    <h1 class="headline headline--top">Members</h1>
    <p class="headline headline--bottom">Wanted</p>

    <p class="drill-band">DRILL EVERY TUESDAY AT 7PM</p>

    <p class="address">
      <svg viewBox="0 0 20 24" aria-hidden="true">
        <path d="M10 1a8 8 0 0 0-8 8c0 6 8 14 8 14s8-8 8-14a8 8 0 0 0-8-8z" fill="none" stroke="var(--red)" stroke-width="2.4"/>
        <circle cx="10" cy="9" r="3" fill="var(--red)"/>
      </svg>
      37 Quarry Bend Lane
    </p>

    <p class="web">
      <svg viewBox="0 0 24 24" aria-hidden="true">
        <circle cx="12" cy="12" r="10.5" fill="var(--navy)"/>
        <path d="M1.5 12h21M12 1.5c-5 5-5 16 0 21M12 1.5c5 5 5 16 0 21M3.5 7h17M3.5 17h17" fill="none" stroke="var(--white)" stroke-width="1.3"/>
      </svg>
      BrookmereCrestFire.example
    </p>

    <p class="dept-name"><span class="dot"></span>Brookmere Crest Fire Department</p>
  </section>
</body>
</html>
```